Engineering group involved with fire safety needs a business card

We need a business card design for a company based in Greece called "Varotis Group". We are engineers and specialized technicians, operating the following : a) Fire fighting equipment trade b) Installation , Inspection & Maintenance of fire extinguishers and fire protection systems c) Occupational Health & Safety (Risk assessment & management/ Staff training). We need a clear and simple card design. I uploaded a draft I made, in order to give you an idea of the company and how I currently imagine the design of the card. I also uploaded the logo in .png file format. We are always open to different, new suggestions and ideas you may want to submit.
Target Market(s)
industries, companies, managers, retail clients
Industry/Entity Type
Fire Safety
Contact Information for Business Card
Addresses & phone numbers (headquarters + branch), logo, name (you can find all the details on the uploaded files!)
Colors
Designer to choose colors to be used in the design.
Look and feel
Each slider illustrates characteristics of the customer's brand and the style your logo design should communicate.

```html
<!DOCTYPE html>
<html lang="en">
<head>
<meta charset="utf-8">
<title>Varotis Group Business Card</title>
<link href="https://fonts.googleapis.com/css2?family=Montserrat:wght@500;600;700&display=swap" rel="stylesheet">
<style>
  :root {
    --canvas: #a4a4a4;
    --slate: #313e43;
    --brand-red: #e52639;
    --deep-red: #a0141e;
    --ink: #313e43;
    --paper: #ffffff;
  }
  * { margin: 0; padding: 0; box-sizing: border-box; }
  html, body { width: 1200px; height: 1200px; overflow: hidden; }
  body {
    background: var(--canvas);
    font-family: "Montserrat", sans-serif;
    position: relative;
  }
  .card {
    position: absolute;
    top: 243px;
    width: 395px;
    height: 709px;
    overflow: hidden;
  }
  .card-front { left: 173px; background: var(--slate); color: var(--paper); }
  .card-back { left: 635px; background: var(--paper); color: var(--ink); }

  .brand-mark {
    position: absolute;
    left: 50%;
    transform: translateX(-50%);
    display: block;
  }
  .brand-name {
    position: absolute;
    left: 0; right: 0;
    text-align: center;
    font-weight: 700;
    letter-spacing: 1px;
  }
  .card-front .brand-mark { top: 195px; width: 80px; height: 80px; background: var(--paper); }
  .card-front .brand-name { top: 298px; font-size: 44px; line-height: 44px; color: var(--paper); }
  .card-back .brand-mark { top: 72px; width: 72px; height: 72px; background: var(--deep-red); }
  .card-back .brand-name { top: 164px; font-size: 38px; line-height: 38px; color: var(--deep-red); }

  .services {
    position: absolute; top: 451px; left: 0; right: 0;
    list-style: none; text-align: center;
    font-size: 13px; font-weight: 600; letter-spacing: 0.4px;
  }
  .services li { line-height: 25px; }

  .web-tab {
    position: absolute; left: 64px; bottom: 0;
    width: 266px; height: 40px;
  }
  .web-address {
    position: absolute; left: 0; right: 0; bottom: 14px;
    text-align: center; font-size: 13px; font-weight: 700; color: var(--paper);
  }

  .person { position: absolute; top: 302px; left: 0; right: 0; text-align: center; }
  .person-name { font-size: 25px; font-weight: 700; letter-spacing: 0.3px; line-height: 30px; }
  .person-role { margin-top: 10px; font-size: 16px; font-weight: 500; color: var(--deep-red); line-height: 20px; }

  .contacts { position: absolute; top: 419px; left: 48px; list-style: none; font-size: 16px; font-weight: 500; }
  .contacts li { display: flex; align-items: center; height: 25.5px; white-space: nowrap; }
  .icon { width: 20px; height: 20px; margin-right: 10px; flex: none; fill: none; stroke: var(--ink); stroke-width: 1.2; }

  .offices { position: absolute; top: 546px; left: 48px; list-style: none; font-size: 16px; }
  .offices li { display: flex; align-items: flex-start; margin-bottom: 10px; line-height: 20px; white-space: nowrap; }
  .offices .icon { margin-top: 2px; margin-right: 11px; }
  .office-label { font-weight: 600; }
  .office-address { font-weight: 500; }
</style>
</head>
<body>
  <section class="card card-front">
    <span class="brand-mark"></span>
    <div class="brand-name">VAROTIS<br>GROUP</div>
    <ul class="services">
      <li>FIRE FIGHTING EQUIPMENT</li>
      <li>LICENSING &amp; BUSINESS REGISTRATION</li>
      <li>OCCUPATIONAL HEALTH &amp; SAFETY</li>
      <li>STAFF TRAINING</li>
    </ul>
    <svg class="web-tab" viewBox="0 0 266 40" aria-hidden="true">
      <path d="M0 40 L18 8 Q22 0 32 0 L234 0 Q244 0 248 8 L266 40 Z" fill="var(--brand-red)"/>
    </svg>
    <div class="web-address">www.varotisgroup.gr</div>
  </section>

  <section class="card card-back">
    <span class="brand-mark"></span>
    <div class="brand-name">VAROTIS<br>GROUP</div>
    <div class="person">
      <div class="person-name">STAVROS MERAKIS</div>
      <div class="person-role">Mechanical Engineer<br>OHS Consultant</div>
    </div>
    <ul class="contacts">
      <li><svg class="icon" viewBox="0 0 20 20"><path d="M4 2 L7 2 L8.5 6 L6.5 7.5 Q8 11.5 12.5 13.5 L14 11.5 L18 13 L18 16 Q17 18 15 18 Q4 16 2 5 Q2 3 4 2 Z"/></svg>+30 22910 45230</li>
      <li><svg class="icon" viewBox="0 0 20 20"><path d="M4 2 L7 2 L8.5 6 L6.5 7.5 Q8 11.5 12.5 13.5 L14 11.5 L18 13 L18 16 Q17 18 15 18 Q4 16 2 5 Q2 3 4 2 Z"/></svg>+30 210 7154420</li>
      <li><svg class="icon" viewBox="0 0 20 20"><rect x="5.5" y="1.5" width="9" height="17" rx="1.5"/><line x1="5.5" y1="4" x2="14.5" y2="4"/><line x1="5.5" y1="15" x2="14.5" y2="15"/><circle cx="10" cy="16.8" r="0.6"/></svg>+30 694 512 73 80</li>
      <li><svg class="icon" viewBox="0 0 20 20"><rect x="1.5" y="4.5" width="17" height="11"/><path d="M1.5 4.5 L10 11 L18.5 4.5 M1.5 15.5 L8 10 M18.5 15.5 L12 10"/></svg>stavros.merakis@varotisgroup.gr</li>
    </ul>
    <ul class="offices">
      <li><svg class="icon" viewBox="0 0 20 20"><path d="M10 19 Q3 11 3 7.5 A7 7 0 0 1 17 7.5 Q17 11 10 19 Z"/><circle cx="10" cy="7.5" r="2.5"/></svg><div><div class="office-label">Headquarters</div><div class="office-address">12 Agiou Nikolaou, 19400 Koropi</div></div></li>
      <li><svg class="icon" viewBox="0 0 20 20"><path d="M10 19 Q3 11 3 7.5 A7 7 0 0 1 17 7.5 Q17 11 10 19 Z"/><circle cx="10" cy="7.5" r="2.5"/></svg><div><div class="office-label">Branch Office</div><div class="office-address">18 Kifisias Avenue, 15125 Marousi</div></div></li>
    </ul>
  </section>
</body>
</html>
```